50 bday

It's my 50th bday and I need the invitation that we will be send by digital (mail and whatapp). One important aspect is that my bday is on day 2 month 2 of year 22 so this is going to be important things that I want to use it as the main theme as you can see in the attached example

```html
<!DOCTYPE html>
<html lang="es">
<head>
<meta charset="utf-8">
<title>Invitación 50 cumpleaños</title>
<link rel="stylesheet" href="https://fonts.googleapis.com/css2?family=Teko:wght@400;500;600;700&family=Kaushan+Script&display=swap">
<style>
  :root {
    --backdrop: #575757;
    --card: #000000;
    --ink: #ffffff;
    --gold-dark: #c29a22;
    --gold-mid: #e0b82c;
    --gold-light: #fffb6e;
    --stripe-orange: #f0871f;
    --stripe-tangerine: #ef5a28;
    --stripe-red: #d7222b;
    --stripe-brown: #3a1a0c;
    --arc-outer: #1a0d08;
    --arc-wine: #621316;
    --arc-rust: #7a3413;
    --arc-amber: #6e4210;
    --burst: #3a2519;
  }
  * { margin: 0; padding: 0; box-sizing: border-box; }
  html, body {
    width: 1200px;
    height: 1200px;
    overflow: hidden;
    background: var(--backdrop);
  }
  .invitation {
    position: absolute;
    left: 190px;
    top: 53px;
    width: 820px;
    height: 1095px;
    background: var(--card);
    overflow: hidden;
  }
  .side-stripes {
    position: absolute;
    top: 0;
    right: 0;
    height: 100%;
    display: flex;
  }
  .side-stripes span { display: block; width: 24px; height: 100%; }
  .side-stripes .orange { background: var(--stripe-orange); }
  .side-stripes .tangerine { background: var(--stripe-tangerine); }
  .side-stripes .red { background: var(--stripe-red); }
  .side-stripes .brown { background: var(--stripe-brown); width: 22px; }

  .age-number {
    position: absolute;
    left: 50px;
    top: 100px;
    width: 250px;
    height: 240px;
    overflow: visible;
  }
  .age-number text {
    font-family: "Teko", sans-serif;
    font-weight: 600;
    fill: var(--ink);
  }
  .headline {
    position: absolute;
    left: 304px;
    top: 146px;
    font-family: "Kaushan Script", cursive;
    font-weight: 400;
    font-size: 64px;
    line-height: 74px;
    color: var(--ink);
    letter-spacing: 0.5px;
    white-space: nowrap;
  }
  .date-burst {
    position: absolute;
    left: 218px;
    top: 343px;
    width: 384px;
    height: 384px;
    border-radius: 50%;
    background: radial-gradient(circle, transparent 34%, var(--burst) 46%, rgba(58,37,25,0.5) 60%, transparent 71%);
    opacity: 0.8;
  }
  .event-date {
    position: absolute;
    left: 190px;
    top: 440px;
    width: 440px;
    height: 200px;
    overflow: visible;
  }
  .event-date text {
    font-family: "Teko", sans-serif;
    font-weight: 500;
  }
  .message {
    position: absolute;
    left: 150px;
    top: 757px;
    width: 512px;
    text-align: center;
    font-family: "Teko", sans-serif;
    font-weight: 400;
    font-size: 38px;
    line-height: 49px;
    color: var(--ink);
  }
  .bottom-arcs {
    position: absolute;
    left: 266px;
    bottom: 0;
    width: 288px;
    height: 144px;
  }
</style>
</head>
<body>
  <main class="invitation">
    <div class="side-stripes" aria-hidden="true">
      <span class="orange"></span>
      <span class="tangerine"></span>
      <span class="red"></span>
      <span class="brown"></span>
    </div>

    <svg class="age-number" viewBox="0 0 250 240" aria-label="50th">
      <text x="4" y="216" font-size="280" textLength="184" lengthAdjust="spacingAndGlyphs">50</text>
      <text x="182" y="43" font-size="44" textLength="30" lengthAdjust="spacingAndGlyphs">TH</text>
    </svg>

    <h1 class="headline">celebración de<br>cumpleaños</h1>

    <div class="date-burst" role="img" aria-label="Destello decorativo de trazos marrones alrededor de la fecha"></div>

    <svg class="event-date" viewBox="0 0 440 200" aria-label="2-2-22">
      <defs>
        <linearGradient id="gold" x1="0" y1="1" x2="1" y2="0">
          <stop offset="0" stop-color="#c29a22"/>
          <stop offset="0.5" stop-color="#e0b82c"/>
          <stop offset="1" stop-color="#fffb6e"/>
        </linearGradient>
      </defs>
      <text x="4" y="171" font-size="225" fill="url(#gold)" textLength="432" lengthAdjust="spacingAndGlyphs">2-2-22</text>
    </svg>

    <p class="message">Reserva desde ahora ese día en tu<br>agenda para juntos compartir en<br>la celebración de mis&nbsp;&nbsp; años</p>

    <svg class="bottom-arcs" viewBox="0 0 288 144" aria-hidden="true">
      <circle cx="144" cy="144" r="144" fill="var(--arc-outer)"/>
      <circle cx="144" cy="144" r="118" fill="var(--arc-wine)"/>
      <circle cx="144" cy="144" r="92" fill="var(--arc-rust)"/>
      <circle cx="144" cy="144" r="66" fill="var(--arc-amber)"/>
      <circle cx="144" cy="144" r="40" fill="var(--card)"/>
    </svg>
  </main>
</body>
</html>
```